Fennel Cellar Online organic artisan and gourmet supermarket

Brief:
Brand: Fennel Cellar (FC) is an online store selling artisan and organinc Italian products. Our look and feel we have gone with is rustic, premium and unfiltered (visit us @ www.fennelcellar.com.au)
Our slogan: "cook Italy, eat Italy, love Italy"
Goals: prior to our online store going live, we used to attend a food market once a week. Due to unfortunate circumstances, we stopped. Since then, our store has gone live and wanted to use the card as a reminder we are back at the markets.
I also have a restaurant, "fennel ristorante" so I wanted to hand them out to customers in the restaurant but also act as reminder of our pop up market stores and our website to buy from.
Personality: FC is more than just a store. Our goal is to be not only a store but an informationa hub of Italian food.
We offer assistance to people who need help in their kitchen as well as catering
Logo: I have a logo which I was not able to upload.

Target Market(s)

Food lovers
Italian food interest
Wealthy
Organic gourmet food enthusiest

Industry/Entity Type

Store

Contact Information for Business Card

Shop online or visit us @ Willow Bend organic market
Ciao@fennelcellar.com.au
Www.fennelcellar.com.au

Online store, Cooking advice, catering, ristorante and information hub

Requirements
Must have
• Logo
• Information
• May be larger than a business card to fit information but smaller than a post card
• Need to look interesting and different
• Not a simple card design
Nice to have
• Different fonts
• Rustic looking
• Qwerky

```html
<!DOCTYPE html>
<html lang="en">
<head>
<meta charset="utf-8">
<title>Fennel Cellar – Business Card</title>
<link rel="stylesheet" href="https://fonts.googleapis.com/css2?family=Montserrat:wght@400;500;600;700&family=Questrial&display=swap">
<style>
  :root {
    --backdrop: #2b2826;
    --card: #1c1c1c;
    --card-back: #222222;
    --ink: #e8e8e8;
    --ink-soft: #bdbdbd;
    --silver: #c9c9c9;
    --green: #1f9a4b;
    --white: #f4f4f4;
    --red: #d8262b;
    --orange: #e8501c;
  }
  * { box-sizing: border-box; margin: 0; padding: 0; }
  html, body { width: 1200px; height: 716px; overflow: hidden; }
  body {
    background: var(--backdrop);
    font-family: "Montserrat", sans-serif;
    color: var(--ink);
    position: relative;
  }
  .card {
    position: absolute;
    top: 200px;
    width: 540px;
    height: 316px;
    border-radius: 3px;
    overflow: hidden;
  }
  .card--front { left: 40px; background: var(--card); }
  .card--back { left: 620px; background: var(--card-back); }

  /* front */
  .brand {
    position: absolute;
    left: 30px; top: 46px;
    width: 220px;
    text-align: center;
  }
  .brand__mark {
    display: block;
    width: 22px; height: 22px;
    margin: 0 auto 10px;
    border: 2px solid var(--ink);
    border-radius: 50%;
  }
  .brand__name {
    font-weight: 700;
    font-size: 17px;
    letter-spacing: 2px;
    text-transform: uppercase;
    color: var(--ink);
  }
  .brand__services {
    margin-top: 12px;
    font-size: 9px;
    line-height: 1.6;
    letter-spacing: 1.2px;
    text-transform: uppercase;
    white-space: nowrap;
    color: var(--ink-soft);
  }
  .tricolour {
    position: absolute;
    left: 258px; top: 0;
    width: 22px; height: 222px;
    display: flex;
  }
  .tricolour span { flex: 1; }
  .tricolour .g { background: var(--green); }
  .tricolour .w { background: var(--white); }
  .tricolour .r { background: var(--red); }

  .person {
    position: absolute;
    left: 305px; top: 70px;
  }
  .person__name {
    font-weight: 500;
    font-size: 19px;
    letter-spacing: 1.5px;
    text-transform: uppercase;
    color: var(--green);
  }
  .person__role {
    margin-top: 4px;
    font-size: 9px;
    font-weight: 600;
    letter-spacing: 1px;
    text-transform: uppercase;
    color: var(--ink);
  }
  .contact {
    list-style: none;
    margin-top: 16px;
    font-size: 10.5px;
    color: var(--ink);
  }
  .contact li { display: flex; align-items: center; gap: 8px; margin-bottom: 7px; }
  .contact svg { width: 11px; height: 11px; flex: none; }

  .visit {
    position: absolute;
    left: 34px; bottom: 34px;
    font-size: 11.5px;
    color: var(--ink);
    line-height: 1.7;
  }
  .visit__market { color: var(--orange); font-weight: 600; }
  .visit__tail { font-weight: 700; }
  .visit__web { font-size: 11px; color: var(--ink-soft); }

  /* back */
  .seal {
    position: absolute;
    left: 0; right: 0; top: 96px;
    text-align: center;
  }
  .seal__mark {
    display: block;
    width: 26px; height: 26px;
    margin: 0 auto 12px;
    border: 2px solid var(--silver);
    border-radius: 50%;
  }
  .seal__name {
    font-weight: 700;
    font-size: 20px;
    letter-spacing: 2.5px;
    text-transform: uppercase;
    color: var(--silver);
  }
  .slogan {
    position: absolute;
    left: 34px; bottom: 40px;
    font-family: "Questrial", sans-serif;
    font-size: 19px;
    letter-spacing: .3px;
    text-transform: uppercase;
  }
  .slogan .cook { color: var(--green); }
  .slogan .eat { color: var(--white); }
  .slogan .love { color: var(--red); }
</style>
</head>
<body>

<section class="card card--front">
  <div class="brand">
    <span class="brand__mark"></span>
    <div class="brand__name">Fennel Cellar</div>
    <div class="brand__services">Online store · Catering<br>Cooking advice · Ristorante<br>Information hub</div>
  </div>

  <div class="tricolour"><span class="g"></span><span class="w"></span><span class="r"></span></div>

  <div class="person">
    <div class="person__name">Marco Bellini</div>
    <div class="person__role">Director</div>
    <ul class="contact">
      <li>
        <svg viewBox="0 0 12 12"><circle cx="6" cy="6" r="6" fill="#1f9a4b"/><path d="M3.6 3.4c.3-.3.7-.3.9 0l.6.8c.2.2.1.5-.1.7l-.3.3c.3.7.9 1.3 1.6 1.6l.3-.3c.2-.2.5-.3.7-.1l.8.6c.3.2.3.6 0 .9l-.4.4c-.5.5-3.8-1.5-4.5-4.5z" fill="#1c1c1c"/></svg>
        Toll free: (02) 8150 3326
      </li>
      <li>
        <svg viewBox="0 0 12 12"><circle cx="6" cy="6" r="6" fill="#1f9a4b"/><rect x="3" y="4" width="6" height="4.2" rx=".4" fill="#1c1c1c"/><path d="M3.2 4.3 6 6.4l2.8-2.1" fill="none" stroke="#1f9a4b" stroke-width=".6"/></svg>
        ciao@fennelcellar.com.au
      </li>
      <li>48 Larkin St, Dunmore, 2046</li>
    </ul>
  </div>

  <div class="visit">
    Shop online or visit us @ <span class="visit__market">Willow Bend</span> <span class="visit__tail">organic market</span><br>
    <span class="visit__web">www.fennelcellar.com.au</span>
  </div>
</section>

<section class="card card--back">
  <div class="seal">
    <span class="seal__mark"></span>
    <div class="seal__name">Fennel Cellar</div>
  </div>
  <p class="slogan"><span class="cook">Cook Italy</span><span class="eat">, Eat Italy, </span><span class="love">Love Italy</span></p>
</section>

</body>
</html>
```